Conservative, Modern and Sharp Builder Business card

Hi there,
We would like to update our existing business card.
I have attached photos of existing business card, logo and van sign.

I would like the business card to also list what we do :
Renovation • New Build • Alteration
Extension • Bathroom • Maintenance.(Seperated by dots)

Contact number : 021 0483 0752
(With that exact spacing)

Ideally when people looking from about 2-3 metres, they know that it is a builder’s business card

Open to suggestions on fonts, layout, style of business card

PLEASE ONLY SUBMIT YOUR BEST OR MAX 3 DESIGNS FOR EACH DESIGNER

Thanks

Industry/Entity Type

Construction. Renovation

Contact Information for Business Card

Details should be the same as the existing card. And addition of what we do.

Requirements
Should not have
• The new business card must not have the same layout as our existing one. Thanks

```html
<!DOCTYPE html>
<html lang="en">
<head>
<meta charset="utf-8">
<title>KeelFrame – Business Card</title>
<link href="https://fonts.googleapis.com/css2?family=Poppins:wght@400;700&family=Questrial&display=swap" rel="stylesheet">
<style>
  :root {
    --page-bg: #e9e7e4;
    --ink: #141414;
    --dark: #1d1e1f;
    --black: #0b0b0b;
    --white: #ffffff;
    --silver-1: #f4f4f4;
    --silver-2: #9a9b9d;
    --silver-3: #d8d8d9;
    --silver-4: #6f7072;
    --muted: #c9c9c9;
  }
  * { margin: 0; padding: 0; box-sizing: border-box; }
  html, body { width: 1200px; height: 900px; overflow: hidden; background: var(--page-bg); }
  .canvas { position: relative; width: 1200px; height: 900px; }
  .card {
    position: absolute; left: 330px; width: 540px; height: 308px;
    overflow: hidden; box-shadow: 0 6px 18px rgba(0,0,0,.22);
  }
  .card--services {
    top: 100px;
    background: linear-gradient(90deg,
      var(--silver-3) 0%, var(--silver-2) 14%, var(--silver-1) 26%,
      var(--silver-4) 40%, var(--silver-3) 52%, var(--silver-1) 62%,
      var(--silver-2) 76%, var(--silver-1) 88%, var(--silver-3) 100%);
  }
  .services {
    position: absolute; left: 42px; top: 92px; list-style: none;
    font-family: "Poppins", sans-serif; font-weight: 700; font-size: 17px;
    color: var(--ink); line-height: 24px;
  }
  .services li::before {
    content: ""; display: inline-block; width: 7px; height: 7px;
    background: var(--ink); transform: rotate(45deg); margin: 0 14px 2px 0;
  }
  .brand {
    position: absolute; font-family: "Poppins", sans-serif; font-weight: 700;
    color: var(--ink); display: flex; align-items: center; gap: 10px;
  }
  .brand__mark { width: 14px; height: 14px; background: var(--ink); }
  .card--services .brand { right: 40px; top: 176px; font-size: 44px; }
  .card--contact { top: 490px; background: var(--dark); }
  .card--contact svg.panels { position: absolute; inset: 0; }
  .card--contact .brand { right: 34px; top: 118px; font-size: 40px; }
  .person { position: absolute; left: 34px; top: 28px; color: var(--white); }
  .person__name { font-family: "Poppins", sans-serif; font-weight: 700; font-size: 15px; letter-spacing: .5px; }
  .person__role { font-family: "Questrial", sans-serif; font-size: 14px; color: var(--muted); }
  .contacts {
    position: absolute; left: 34px; bottom: 28px; list-style: none;
    font-family: "Questrial", sans-serif; font-size: 14px; color: var(--white); line-height: 22px;
  }
  .contacts li { display: flex; align-items: center; gap: 9px; }
  .contacts .phone { font-family: "Poppins", sans-serif; font-weight: 700; font-size: 17px; }
  .contacts svg { width: 13px; height: 13px; flex: none; }
</style>
</head>
<body>
<main class="canvas">
  <section class="card card--services">
    <ul class="services">
      <li>Renovation</li>
      <li>New Build</li>
      <li>Alteration</li>
      <li>Extension</li>
      <li>Bathroom</li>
      <li>Maintenance</li>
    </ul>
    <div class="brand"><span class="brand__mark"></span>KeelFrame</div>
  </section>

  <section class="card card--contact">
    <svg class="panels" viewBox="0 0 540 308" width="540" height="308">
      <defs>
        <linearGradient id="steel" x1="0" y1="0" x2="1" y2="0">
          <stop offset="0" stop-color="#6f7072"/>
          <stop offset=".35" stop-color="#f2f2f2"/>
          <stop offset=".6" stop-color="#8d8e90"/>
          <stop offset="1" stop-color="#e6e6e6"/>
        </linearGradient>
      </defs>
      <polygon points="0,0 540,0 540,12 300,12 150,100 0,100" fill="var(--black)"/>
      <polygon points="120,100 290,0 540,0 540,270 120,130" fill="url(#steel)"/>
      <polygon points="160,112 305,14 540,14 540,256" fill="var(--white)"/>
      <polygon points="0,100 120,100 540,272 540,308 0,308" fill="var(--dark)"/>
    </svg>
    <div class="person">
      <div class="person__name">MARLO TENNEY</div>
      <div class="person__role">Residential Builder</div>
    </div>
    <div class="brand"><span class="brand__mark"></span>KeelFrame</div>
    <ul class="contacts">
      <li class="phone">
        <svg viewBox="0 0 24 24"><path fill="#fff" d="M6.6 10.8a15 15 0 0 0 6.6 6.6l2.2-2.2c.3-.3.7-.4 1-.2 1.1.4 2.3.6 3.6.6.6 0 1 .4 1 1V20c0 .6-.4 1-1 1A17 17 0 0 1 3 4c0-.6.4-1 1-1h3.5c.6 0 1 .4 1 1 0 1.3.2 2.5.6 3.6.1.3 0 .7-.2 1z"/></svg>
        021 0483 0752
      </li>
      <li>
        <svg viewBox="0 0 24 24"><rect x="2" y="5" width="20" height="14" rx="2" fill="#fff"/><path d="M3 6l9 7 9-7" stroke="#1d1e1f" stroke-width="2" fill="none"/></svg>
        hello@keelframe.co.nz
      </li>
      <li>
        <svg viewBox="0 0 24 24"><circle cx="12" cy="12" r="9" stroke="#fff" stroke-width="2" fill="none"/><path d="M3 12h18M12 3c3 3 3 15 0 18M12 3c-3 3-3 15 0 18" stroke="#fff" stroke-width="1.5" fill="none"/></svg>
        www.keelframe.co.nz
      </li>
      <li>
        <svg viewBox="0 0 24 24"><circle cx="12" cy="12" r="9" fill="#fff"/></svg>
        keelframe.nz
      </li>
    </ul>
  </section>
</main>
</body>
</html>
```